Stylish Business Card for Modern hair salon

I need a simple business card design using our salon logo and colours that are in the logo. We service clients of all ages but predominantly those in the 18 to 55 age range. We have a young staff and are looking to have a card that will present a modern and clean image that represents who we are. The card should be in black and white same as our logo. Minimal use of other colours is allowed.

Industry/Entity Type

Hair And Beauty

Contact Information for Business Card

The design should have the following information
salon name - TR Hair Studio
address - 2751 Birchfield Rd.E. Brookhaven, BV L7P3K2
phone - 905 614-2870
website - trhairexample.ca
instagram - tr.hairstudio
twitter - @TR_HairStudio

Colors
000000
ffffff
474747

Requirements
Must have
• simple design, salon name, address, phone, website, instagram, twitter info
• Back of card should have the following:
• YOUR NEXT APPOINTMENT
• DATE
• TIME
Nice to have
• simple design, clear to see and read,
• predominantly black and white colour, minimal use of other colours is ok
Should not have
• many colours, various fonts

```html
<!DOCTYPE html>
<html lang="en">
<head>
<meta charset="utf-8">
<title>TR Hair Studio — Business Card</title>
<link href="https://fonts.googleapis.com/css2?family=Cormorant+Garamond:wght@400;600&display=swap" rel="stylesheet">
<style>
  :root {
    --ink: #000000;
    --paper: #ffffff;
    --grey: #474747;
    --backdrop: #e6e6e6;
  }
  * { margin: 0; padding: 0; box-sizing: border-box; }
  html, body { width: 1200px; height: 900px; overflow: hidden; }
  body {
    background: var(--backdrop);
    font-family: "Cormorant Garamond", Georgia, serif;
    position: relative;
  }
  .card {
    position: absolute;
    width: 630px;
    height: 360px;
    box-shadow: 0 6px 18px rgba(0,0,0,0.18);
  }
  .card--front {
    left: 140px; top: 60px;
    background: var(--paper);
    color: var(--ink);
  }
  .card--back {
    left: 430px; top: 480px;
    background: var(--ink);
    color: var(--paper);
  }
  .brand-name {
    position: absolute;
    top: 60px; left: 0; right: 0;
    text-align: center;
    font-size: 52px;
    font-weight: 600;
    letter-spacing: 2px;
    line-height: 1;
  }
  .appointment-title {
    position: absolute;
    top: 170px; left: 0; right: 0;
    text-align: center;
    font-size: 22px;
  }
  .field {
    position: absolute;
    display: flex;
    align-items: flex-end;
    gap: 12px;
    font-size: 22px;
    line-height: 1;
  }
  .field__line {
    border-bottom: 1px solid var(--ink);
    height: 1px;
    margin-bottom: 3px;
  }
  .field--date { left: 60px; top: 235px; }
  .field--date .field__line { width: 250px; }
  .field--time { left: 385px; top: 235px; }
  .field--time .field__line { width: 150px; }
  .contact {
    position: absolute;
    right: 40px; bottom: 40px;
    width: 440px;
    text-align: center;
    font-size: 18px;
    line-height: 1.35;
  }
  .socials {
    display: flex;
    justify-content: center;
    gap: 28px;
    margin-top: 6px;
    font-size: 15px;
  }
  .social { display: flex; align-items: center; gap: 7px; }
  .social__dot {
    width: 9px; height: 9px;
    border-radius: 50%;
    background: var(--paper);
  }
</style>
</head>
<body>
  <section class="card card--front" aria-label="Card front">
    <div class="brand-name">TR Hair Studio</div>
    <div class="appointment-title">Next Appointment</div>
    <div class="field field--date"><span>Date</span><span class="field__line"></span></div>
    <div class="field field--time"><span>Time</span><span class="field__line"></span></div>
  </section>

  <section class="card card--back" aria-label="Card back">
    <div class="contact">
      <p>2751 Birchfield Rd.E. Brookhaven, BV L7P3K2</p>
      <p>Phone. 555 614-2870 | www.trhairexample.ca</p>
      <div class="socials">
        <span class="social"><span class="social__dot"></span>tr.hairstudio</span>
        <span class="social"><span class="social__dot"></span>@TR_HairStudio</span>
      </div>
    </div>
  </section>
</body>
</html>
```